Veteran Owned General Contractor needs Bold New Business Cards

We are a service disabled veteran owned small business. We're a general contractor that specializes in excavation, underground utilities, site work, land clearing and demolition. We would like a fresh, simple, bold, new look for our business cards. We're open to ideas! We'd like to incorporate the following information on the card:

Company Name & Logo, Name of Person, Job Title, Office Phone, Fax, Cell Phone, Email Address, Website, SDVOSB

Our logo is included. We look forward to your thoughts.

Thank you!
Updates

Reason: Hello Due to the overwhelming response to this project, we are extending the deadline one time to allow for improved communication and feedback with the top candidates. We would like to thank everyone for their hard work and exceptional creativity! Thank you

Industry/Entity Type

Business

Contact Information for Business Card

Font styles to use
Sans Serif

Requirements
Nice to have
• As we are a veteran owned company, it would be nice to incorporate an American flag into the design. Maybe on the back?

```html
<!DOCTYPE html>
<html lang="en">
<head>
<meta charset="utf-8">
<title>Ironvale Works Inc – Business Card</title>
<link rel="stylesheet" href="https://fonts.googleapis.com/css2?family=Questrial&display=swap">
<style>
  :root {
    --backdrop: #1c1c1c;
    --card: #f4f4f3;
    --green: #6cbf45;
    --grey: #8a8a8c;
    --ink: #333333;
    --dark-tile: #2e2f2e;
    --flag-navy: #1f2f78;
    --flag-red: #b71f27;
    --flag-white: #eeeeee;
    --mark-red: #b3141c;
  }
  * { margin: 0; padding: 0; box-sizing: border-box; }
  html, body { width: 1200px; height: 1200px; overflow: hidden; }
  body {
    background: var(--backdrop);
    font-family: "Questrial", sans-serif;
    position: relative;
  }
  .card {
    position: absolute;
    left: 204px;
    width: 792px;
    height: 452px;
    background: var(--card);
    overflow: hidden;
  }
  .card--front { top: 111px; }
  .card--back { top: 636px; }
  .card svg.waves { position: absolute; inset: 0; width: 792px; height: 452px; }

  .brand {
    position: absolute;
    display: flex;
    flex-direction: column;
    align-items: center;
    gap: 22px;
  }
  .brand__square {
    width: 78px; height: 78px;
    border-radius: 10px;
    background: var(--dark-tile);
  }
  .brand__name {
    font-size: 40px;
    letter-spacing: 2px;
    white-space: nowrap;
    line-height: 1;
  }
  .card--front .brand { left: 30px; width: 340px; top: 152px; }
  .card--front .brand__name { color: var(--green); font-size: 34px; }

  .divider {
    position: absolute;
    left: 396px; top: 115px;
    width: 2px; height: 224px;
    background: var(--grey);
  }
  .person { position: absolute; left: 444px; top: 88px; }
  .person__name {
    color: var(--green);
    font-size: 30px;
    letter-spacing: 0.5px;
    line-height: 1.1;
  }
  .person__title {
    color: var(--ink);
    font-size: 24px;
    letter-spacing: 3px;
    margin-top: 4px;
  }
  .contacts { position: absolute; left: 444px; top: 190px; list-style: none; }
  .contacts li {
    display: flex; align-items: center; gap: 10px;
    font-size: 23px; color: var(--ink);
    height: 32px;
  }
  .contacts li.gap { margin-top: 10px; }
  .contacts svg { width: 26px; height: 26px; flex: none; }

  .card--back .brand { left: 430px; width: 320px; top: 132px; gap: 26px; }
  .card--back .brand__name { color: var(--mark-red); font-size: 38px; }
</style>
</head>
<body>

<section class="card card--front" aria-label="Business card front">
  <svg class="waves" viewBox="0 0 792 452" aria-hidden="true">
    <path fill="var(--grey)" d="M0 82 C150 38 350 18 520 44 C640 62 700 56 792 24 L792 30 C700 64 640 70 520 52 C350 26 150 46 0 92 Z"/>
    <path fill="var(--green)" d="M0 98 C150 66 330 50 500 60 C560 63 600 66 640 64 C560 70 500 68 440 66 C300 62 150 78 0 106 Z"/>
    <path fill="var(--green)" d="M0 410 C200 366 400 388 560 394 C680 398 740 380 792 352 L792 372 C730 400 660 412 560 408 C400 400 200 382 0 418 Z"/>
    <path fill="var(--grey)" d="M0 424 C200 390 380 404 560 418 C680 426 740 410 792 384 L792 392 C740 420 680 436 560 428 C380 414 200 398 0 430 Z"/>
  </svg>

  <div class="brand">
    <div class="brand__square"></div>
    <div class="brand__name">IRONVALE WORKS INC</div>
  </div>

  <div class="divider"></div>

  <div class="person">
    <div class="person__name">NAME OF PERSON</div>
    <div class="person__title">Your Job Title</div>
  </div>

  <ul class="contacts">
    <li>
      <svg viewBox="0 0 26 26" aria-hidden="true"><rect width="26" height="26" rx="4" fill="var(--green)"/><path d="M8 6 L11 6 L12 10 L10 11.5 C11 14 12 15 14.5 16 L16 14 L20 15 L20 18 C14 19 7 12 8 6 Z" fill="#fff"/></svg>
      07700 900418
    </li>
    <li>
      <svg viewBox="0 0 26 26" aria-hidden="true"><rect width="26" height="26" rx="4" fill="var(--green)"/><rect x="6" y="8" width="14" height="11" rx="1.5" fill="none" stroke="#fff" stroke-width="1.8"/><rect x="15" y="10" width="3" height="7" fill="#fff"/><rect x="8" y="11" width="2" height="2" fill="#fff"/><rect x="11" y="11" width="2" height="2" fill="#fff"/><rect x="8" y="14" width="2" height="2" fill="#fff"/><rect x="11" y="14" width="2" height="2" fill="#fff"/></svg>
      0207 946 0321
    </li>
    <li>
      <svg viewBox="0 0 26 26" aria-hidden="true"><rect width="26" height="26" rx="4" fill="var(--green)"/><rect x="8.5" y="5" width="9" height="16" rx="1.5" fill="none" stroke="#fff" stroke-width="1.8"/><circle cx="13" cy="18" r="1" fill="#fff"/></svg>
      0207 946 0788
    </li>
    <li class="gap">
      <svg viewBox="0 0 26 26" aria-hidden="true"><rect width="26" height="26" rx="4" fill="var(--green)"/><rect x="6" y="8" width="14" height="10" fill="none" stroke="#fff" stroke-width="1.6"/><path d="M6 8 L13 14 L20 8" fill="none" stroke="#fff" stroke-width="1.6"/></svg>
      youremail@mailbox.com
    </li>
    <li>
      <svg viewBox="0 0 26 26" aria-hidden="true"><rect width="26" height="26" rx="4" fill="var(--green)"/><circle cx="13" cy="13" r="7" fill="none" stroke="#fff" stroke-width="1.6"/><path d="M6 13 H20 M13 6 C10 10 10 16 13 20 M13 6 C16 10 16 16 13 20" fill="none" stroke="#fff" stroke-width="1.2"/></svg>
      ironvaleworks.com
    </li>
  </ul>
</section>

<section class="card card--back" aria-label="Business card back">
  <svg class="waves" viewBox="0 0 792 452" aria-hidden="false">
    <defs>
      <linearGradient id="flag-tones" x1="0" y1="0" x2="1" y2="0">
        <stop offset="0" stop-color="var(--flag-navy)"/>
        <stop offset="0.36" stop-color="var(--flag-navy)"/>
        <stop offset="0.46" stop-color="var(--flag-red)"/>
        <stop offset="0.62" stop-color="var(--flag-white)"/>
        <stop offset="0.8" stop-color="var(--flag-red)"/>
        <stop offset="1" stop-color="var(--flag-white)"/>
      </linearGradient>
    </defs>
    <path role="img" aria-label="Waving American flag" fill="url(#flag-tones)"
          d="M0 100 C150 64 330 50 500 58 C640 64 700 56 792 26 L792 360 C740 388 680 404 560 402 C400 398 200 380 0 414 Z"/>
    <path fill="var(--grey)" d="M0 82 C150 38 350 18 520 44 C640 62 700 56 792 24 L792 30 C700 64 640 70 520 52 C350 26 150 46 0 92 Z"/>
    <path fill="var(--green)" d="M0 98 C150 62 330 48 500 56 C640 62 700 54 792 28 L792 34 C700 62 640 68 500 62 C330 56 150 72 0 108 Z"/>
    <path fill="var(--green)" d="M0 410 C200 366 400 388 560 394 C680 398 740 380 792 352 L792 372 C730 400 660 412 560 408 C400 400 200 382 0 418 Z"/>
    <path fill="var(--grey)" d="M0 424 C200 390 380 404 560 418 C680 426 740 410 792 384 L792 392 C740 420 680 436 560 428 C380 414 200 398 0 430 Z"/>
  </svg>

  <div class="brand">
    <div class="brand__square"></div>
    <div class="brand__name">IRONVALE WORKS</div>
  </div>
</section>

</body>
</html>
```